Business Card Design Project for Architecture and Interior Design company

We need a business card design and logo for an architecture and design firm located in Santiago de Chile. It´s a small company, and the name is "Vostiq" ("Vost" from my surname Vostani, and "arq" for arquitectura or architecture. But it would also be nice that the logo comunicates de Word game "Vosta" as beautiful in italian, and "arq" as architecture".
The idea is to give a delicate, elegant and sofisticated, yet fresh image. Would prefer grey black and white colors, but wouldn´t mind to use another additional color.
I allready have a web page www.vostiq.cl, but would like to improve the logo design.
Please contact if any further information is requiered.
Reason: Need a more arquitectural and desing spirit in the cards. Few of them give that idea.

```html
<!DOCTYPE html>
<html lang="es">
<head>
<meta charset="utf-8">
<title>Vostiq — Tarjeta de presentación</title>
<link rel="stylesheet" href="https://fonts.googleapis.com/css2?family=Questrial&family=Roboto:ital,wght@1,400;1,500&display=swap">
<style>
  :root {
    --backdrop: #2b2a29;
    --card-grey: #707071;
    --card-grey-dark: #5c5c5d;
    --ink-dark: #1c1c1d;
    --ink-light: #f4f4f4;
    --ink-soft: #e0e0e0;
    --accent-light: #dcdcdc;
  }
  * { box-sizing: border-box; margin: 0; padding: 0; }
  html, body {
    width: 1200px;
    height: 900px;
    overflow: hidden;
    background: var(--backdrop);
  }
  .sheet {
    position: relative;
    width: 1200px;
    height: 900px;
  }
  .card {
    position: absolute;
    left: 300px;
    width: 600px;
    height: 343px;
    background: linear-gradient(135deg, var(--card-grey) 0%, var(--card-grey-dark) 100%);
    box-shadow: 0 10px 28px rgba(0, 0, 0, 0.45);
  }
  .card--front { top: 80px; }
  .card--back { top: 477px; }

  .brand {
    position: absolute;
    display: flex;
    align-items: center;
    gap: 22px;
  }
  .card--front .brand { left: 150px; top: 128px; }
  .card--back .brand { left: 52px; top: 205px; }

  .brand__square {
    width: 58px;
    height: 58px;
    background: var(--accent-light);
    flex: none;
  }
  .brand__name {
    font-family: "Questrial", "Helvetica Neue", sans-serif;
    font-weight: 400;
    font-size: 64px;
    color: var(--ink-dark);
    letter-spacing: 1.5px;
    line-height: 1;
  }

  .contact {
    position: absolute;
    left: 344px;
    top: 38px;
    width: 240px;
    font-family: "Roboto", Arial, sans-serif;
    font-style: italic;
    color: var(--ink-light);
  }
  .contact__name {
    font-size: 18px;
    font-weight: 500;
    letter-spacing: 0.4px;
    white-space: nowrap;
  }
  .contact__role {
    font-size: 12px;
    color: var(--ink-soft);
    letter-spacing: 0.6px;
    margin: 4px 0 20px 2px;
  }
  .contact__list {
    list-style: none;
    font-size: 13px;
    line-height: 1.55;
    letter-spacing: 0.4px;
  }
  .contact__label { color: var(--ink-soft); }
</style>
</head>
<body>
  <main class="sheet">
    <section class="card card--front" aria-label="Anverso de la tarjeta">
      <div class="brand">
        <span class="brand__square" aria-hidden="true"></span>
        <span class="brand__name">Vostiq</span>
      </div>
    </section>

    <section class="card card--back" aria-label="Reverso de la tarjeta">
      <div class="contact">
        <p class="contact__name">Anjali Vostani Ruiz</p>
        <p class="contact__role">Arquitecto</p>
        <ul class="contact__list">
          <li><span class="contact__label">Mob:</span> +56 9 41502738</li>
          <li><span class="contact__label">mail:</span> avostani@vostiq.cl</li>
          <li><span class="contact__label">Web:</span> www.vostiq.cl</li>
        </ul>
      </div>
      <div class="brand">
        <span class="brand__square" aria-hidden="true"></span>
        <span class="brand__name">Vostiq</span>
      </div>
    </section>
  </main>
</body>
</html>
```